Bar Wanderlust VIP Card design

Looking for a design for a VIP card forguests wishing to purchase to avoid cover charges, skipping the line and othe advantages.

We used our logo on last years card.I've also attached a few of our previous cards. Looking for something fresh.

We are not apposed to a vertical card either way would be fine We will have to incorporate the kelp fizz logo on the card as well.

Industry/Entity Type

Bar Restaurant www.tavern-quillo.example

Font styles to use
Decorative

```html
<!DOCTYPE html>
<html lang="en">
<head>
<meta charset="utf-8">
<title>Bar Wanderlust VIP Card</title>
<link rel="stylesheet" href="https://fonts.googleapis.com/css2?family=Libre+Baskerville:wght@400;700&display=swap">
<style>
  :root {
    --stage: #0d0366;
    --card-white: #f4f8fc;
    --mosaic-green: #7fa98a;
    --mosaic-sky: #a9d3ee;
    --mosaic-blue: #5f86cf;
    --mosaic-lilac: #d4d6ee;
    --gold: #d9a21e;
    --gold-deep: #b98313;
    --year-blue: #3f6cb8;
    --brand-slate: #5d7077;
    --partner-blue: #2e3a9c;
  }
  * { margin: 0; padding: 0; box-sizing: border-box; }
  html, body { width: 1200px; height: 1200px; overflow: hidden; }
  body {
    background: var(--stage);
    position: relative;
    font-family: "Libre Baskerville", "Times New Roman", serif;
  }
  .vip-card {
    position: absolute;
    left: 210px; top: 383px;
    width: 778px; height: 445px;
    border-radius: 17px;
    overflow: hidden;
    box-shadow: 4px 6px 10px rgba(0, 0, 0, 0.35);
  }
  .card-backdrop {
    position: absolute; inset: 0;
    background:
      radial-gradient(ellipse 45% 60% at 50% 40%, var(--card-white) 0%, rgba(244,248,252,0) 100%),
      radial-gradient(ellipse 40% 50% at 5% 95%, var(--mosaic-green) 0%, rgba(127,169,138,0) 100%),
      radial-gradient(ellipse 35% 45% at 10% 15%, var(--mosaic-lilac) 0%, rgba(212,214,238,0) 100%),
      linear-gradient(90deg, #e6ecf2 0%, #eef3f7 35%, var(--mosaic-sky) 70%, var(--mosaic-blue) 100%);
  }
  .partner-mark {
    position: absolute;
    left: 640px; top: 30px;
    width: 102px; height: 52px;
    display: flex; align-items: center; justify-content: center;
    color: var(--partner-blue);
    font-weight: 700;
    font-size: 16px;
    line-height: 1.05;
    text-align: center;
    text-transform: uppercase;
  }
  .venue-brand {
    position: absolute;
    left: 0; right: 0; top: 140px;
    display: flex; align-items: center; justify-content: center;
    gap: 16px;
  }
  .venue-brand .brand-dot {
    width: 54px; height: 54px;
    border-radius: 50%;
    background: var(--brand-slate);
  }
  .venue-brand .brand-name {
    color: var(--brand-slate);
    font-weight: 700;
    font-size: 34px;
    letter-spacing: 1px;
    text-transform: uppercase;
  }
  .membership {
    position: absolute;
    left: 271px; top: 342px;
    display: flex; align-items: center;
  }
  .membership .tier {
    font-size: 82px;
    line-height: 1;
    color: var(--gold);
    background: linear-gradient(180deg, #f0c040 0%, var(--gold) 50%, var(--gold-deep) 100%);
    -webkit-background-clip: text;
    background-clip: text;
    -webkit-text-fill-color: transparent;
  }
  .membership .season {
    margin-left: 18px;
    width: 98px;
    border-top: 2px solid var(--gold);
    border-bottom: 2px solid var(--gold);
    padding: 12px 0 10px;
    text-align: center;
    font-size: 27px;
    color: var(--year-blue);
  }
</style>
</head>
<body>
  <div class="vip-card">
    <div class="card-backdrop" role="img" aria-label="Soft geometric mosaic of pale triangles shading from green and lilac on the left to sky and deep blue on the right"></div>
    <div class="partner-mark">Kelp<br>Fizz</div>
    <div class="venue-brand">
      <span class="brand-dot"></span>
      <span class="brand-name">Bar Wanderlust</span>
    </div>
    <div class="membership">
      <span class="tier">VIP</span>
      <span class="season">2023</span>
    </div>
  </div>
</body>
</html>
```